Home page for Quill Helper

Develop the home page for QuillHelper.co, which is an AI-powered chatbot platform that allows users to add an educated chatbot to their websites to assist customers with questions and other inquiries.

The hero banner should contain the text:

"Instantly create a FREE AI Chatbot for your website! Just enter the URL of your website below and the chatbot will educate itself about your business"

Below this text should be an text box to enter the URL of the visitor's website.

The platform is a subsidiary of PageLoomX.com, so the theme should be very similar to the website pageloomx.com.

I have attached the content for the page, a mockup of the hero banner section, and videos for the hero banner.

```html
<!DOCTYPE html>
<html lang="en">
<head>
<meta charset="utf-8">
<title>Quill Helper</title>
<link href="https://fonts.googleapis.com/css2?family=Source+Sans+3:wght@400;600;700&family=Poppins:wght@500;600&display=swap" rel="stylesheet">
<style>
:root{
  --blue:#5e93f3;
  --blue-soft:#6a9bf4;
  --ink:#1d2431;
  --muted:#4a5160;
  --navy:#1e3a5c;
  --cta:#1f3865;
  --footer:#0a2444;
  --white:#ffffff;
  --line:#e6e9ef;
  --star:#f7b500;
}
*{box-sizing:border-box;margin:0;padding:0}
html,body{width:670px;height:1200px;overflow:hidden;background:var(--white)}
body{font-family:"Source Sans 3",sans-serif;color:var(--ink)}
.page{position:relative;width:670px;height:1200px;overflow:hidden}
.abs{position:absolute}
.center{left:0;right:0;text-align:center}
.eyebrow{font-size:5px;font-weight:600;letter-spacing:.1px;color:var(--blue);line-height:6px}
.section-title{font-size:9.5px;line-height:12px;font-weight:400}
.accent{color:var(--blue)}
.rule{height:1.4px;width:42px;left:314px;background:var(--blue)}

/* features */
.feature-card{top:74px;width:147px;height:136px;border-radius:9px;background:var(--white);box-shadow:0 1px 6px rgba(40,60,100,.08);text-align:center}
.feature-icon{position:absolute;top:18px;left:59.5px;width:28px;height:28px}
.feature-title{position:absolute;top:62px;left:0;right:0;font-size:6.6px;font-weight:700;line-height:8px}
.feature-text{position:absolute;top:77px;left:6px;right:6px;font-size:5.4px;line-height:9.8px;color:var(--muted)}
.feature-text b{color:var(--ink);font-weight:700}

/* testimonials */
.testimonials-back{left:101px;top:252px;width:467px;height:210px;border-radius:10px;background:var(--navy)}
.testimonials{left:101px;top:259px;width:467px;height:203px;border-radius:10px;background:var(--blue-soft)}
.testimonials .eyebrow{color:var(--white)}
.testimonials .section-title{color:var(--white)}
.quote-card{top:337.6px;width:134px;height:103.5px;border-radius:14px;background:var(--navy);color:var(--white);text-align:center}
.stars{position:absolute;top:13px;left:0;right:0;font-size:6px;line-height:7px;color:var(--star);letter-spacing:1px}
.quote{position:absolute;top:27px;left:8px;right:8px;font-size:5.4px;line-height:9.8px}
.quote-rule{position:absolute;top:63.5px;left:14px;right:14px;height:.5px;background:rgba(255,255,255,.25)}
.quote-name{position:absolute;top:73px;left:0;right:0;font-size:5.4px;font-weight:700;line-height:7px}
.quote-role{position:absolute;top:84px;left:0;right:0;font-size:5.4px;line-height:7px}

/* cta */
.cta-shape{left:101px;top:540px;width:467px;height:220px}
.robot{left:135px;top:499px;width:168px;height:252px;border-radius:60px 60px 40px 70px;background:radial-gradient(circle at 40% 35%,#f4f5fa 0%,#d5d8e6 45%,#8c93ad 80%,#3d4a6a 100%)}
.cta-title{left:326px;top:603px;font-size:12px;font-weight:700;line-height:14px;color:var(--white)}
.cta-text{left:326px;width:222px;font-size:5.5px;line-height:9.8px;color:var(--white)}
.cta-button{left:326px;top:715px;width:84px;height:15px;border-radius:1.5px;background:var(--blue);color:var(--white);font-size:5.5px;font-weight:600;line-height:15px;text-align:center}

/* faq */
.faq{left:182px;top:858px;width:306px;height:128px;border-radius:9px;background:var(--white);box-shadow:0 1px 6px rgba(40,60,100,.08)}
.faq-q{position:absolute;left:13px;right:30px;font-size:6.5px;font-weight:600;line-height:8px}
.faq-q.open{color:var(--blue)}
.faq-toggle{position:absolute;left:286px;width:6px;height:6px}
.faq-divider{position:absolute;left:13px;right:13px;height:.5px;background:var(--line)}
.faq-a{position:absolute;left:12px;top:53.5px;font-size:5.4px;line-height:7px;color:var(--muted)}
.closing{top:1001px;font-size:5.8px;line-height:9.8px}

/* footer */
.footer{left:0;top:1055px;width:670px;height:145px;background:var(--footer);color:var(--white)}
.brand{position:absolute;left:137px;top:30px;font-size:12px;font-weight:600;line-height:15px}
.tagline{position:absolute;left:137px;top:57px;width:95px;font-size:6px;line-height:9.8px}
.copyright{position:absolute;left:137px;top:101px;width:90px;font-size:6px;line-height:9.8px}
.footer-col{position:absolute;top:28px}
.footer-col h3{font-family:"Poppins",sans-serif;font-size:7.3px;font-weight:500;line-height:9px;margin-bottom:5px}
.footer-col ul{list-style:none}
.footer-col li{font-size:5.3px;line-height:9.8px}
.social{display:flex;flex-wrap:wrap;width:60px;gap:5px 5.5px;margin-top:3px}
.social span{width:6.5px;height:6.5px;border-radius:50%;background:var(--white)}
</style>
</head>
<body>
<div class="page">

  <!-- Features -->
  <div class="abs center eyebrow" style="top:15px">ADVANCED FEATURES</div>
  <h2 class="abs center section-title" style="top:24px">Advanced Features That Set <span class="accent">Quill Helper</span> Apart.</h2>
  <div class="abs rule" style="top:44px"></div>

  <div class="abs feature-card" style="left:101px">
    <svg class="feature-icon" viewBox="0 0 28 28" fill="none" stroke="#5e93f3" stroke-width="0.9" stroke-linecap="round" stroke-linejoin="round">
      <path d="M9 19 L7 17 C10 14 9 9 13 7 C16 5.5 20 7 21 10 C22 14 19 17 20 21 L18 22 Z"/>
      <path d="M11 21 C11 23 13 24 14.5 23"/>
      <circle cx="16" cy="5.5" r="1"/>
      <path d="M22 6 C24 8 24.5 10 24 12"/>
      <path d="M6 9 C5 11 5 13 6 15"/>
    </svg>
    <div class="feature-title">Real-Time Notifications</div>
    <p class="feature-text">Stay on top of customer interactions with text<br>and email alerts for new inquiries. Never miss a<br>chance to connect with your customers whether<br>you're in the office or on the go.</p>
  </div>

  <div class="abs feature-card" style="left:262px">
    <svg class="feature-icon" viewBox="0 0 28 28" fill="none" stroke="#5e93f3" stroke-width="0.9" stroke-linecap="round" stroke-linejoin="round">
      <rect x="6" y="2" width="14" height="24" rx="2"/>
      <circle cx="11" cy="10" r="2.5"/>
      <path d="M7 16 C8 13.5 14 13.5 15 16"/>
      <path d="M9 19 H16 M9 21.5 H14"/>
      <rect x="15" y="6" width="7" height="3" rx="1.5"/>
      <circle cx="22" cy="18" r="2.5"/>
      <path d="M22 14 V15.2 M22 20.8 V22 M18 18 H19.2 M24.8 18 H26"/>
    </svg>
    <div class="feature-title">Mobile App Access</div>
    <p class="feature-text">Monitor your bot's activity and interact with<br>customers directly through our mobile app.<br>Whether you're at a meeting or traveling, you're<br>always connected.</p>
  </div>

  <div class="abs feature-card" style="left:422px">
    <svg class="feature-icon" viewBox="0 0 28 28" fill="none" stroke="#5e93f3" stroke-width="0.9" stroke-linecap="round" stroke-linejoin="round">
      <rect x="2" y="2" width="22" height="22" rx="1.5"/>
      <path d="M2 6.5 H24"/>
      <circle cx="16" cy="4.3" r=".7"/><circle cx="18.5" cy="4.3" r=".7"/><circle cx="21" cy="4.3" r=".7"/>
      <path d="M5 11 H20 M5 15 H18 M5 19 H14"/>
      <circle cx="10" cy="11" r="1.3"/><circle cx="15" cy="15" r="1.3"/><circle cx="8" cy="19" r="1.3"/>
      <path d="M18 17 L18 27 L20.5 24.5 L22.5 28 L24 27 L22 23.5 L25.5 23.5 Z" fill="#fff"/>
    </svg>
    <div class="feature-title">Customizable Plans</div>
    <p class="feature-text"><b>Free Plan</b>: Perfect for smaller or newer businesses.<br><b>Business Plans</b>: Scaled for growing enterprises<br>with advanced features.<br><b>Agency Plan</b>: Allows unlimited chatbot creation<br>for digital agencies.</p>
  </div>

  <!-- Testimonials -->
  <div class="abs testimonials-back"></div>
  <div class="abs testimonials"></div>
  <div class="abs center eyebrow" style="top:279px;color:var(--white)">TESTIMONIALS</div>
  <h2 class="abs center section-title" style="top:288px;color:var(--white)">Why Businesses Love Quill Helper</h2>
  <div class="abs rule" style="top:308px;background:var(--white)"></div>

  <div class="abs quote-card" style="left:122px">
    <div class="stars">★★★★★</div>
    <p class="quote">"Quill Helper transformed our customer<br>support. It's like having an extra team<br>member who works 24/7!"</p>
    <div class="quote-rule"></div>
    <div class="quote-name">Nora P.</div>
    <div class="quote-role">Small Business Owner</div>
  </div>
  <div class="abs quote-card" style="left:268px">
    <div class="stars">★★★★★</div>
    <p class="quote">"The human assistance option is a game<br>changer. Our team loves the flexibility of<br>jumping in when needed."</p>
    <div class="quote-rule"></div>
    <div class="quote-name">Daniel W.</div>
    <div class="quote-role">Enterprise Manager</div>
  </div>
  <div class="abs quote-card" style="left:413.6px">
    <div class="stars">★★★★★</div>
    <p class="quote">"Setting up Quill Helper was so simple, and<br>the results were instant. Our customers are<br>more engaged than ever."</p>
    <div class="quote-rule"></div>
    <div class="quote-name">Ivy M.</div>
    <div class="quote-role">Digital Marketer</div>
  </div>

  <!-- Call to action -->
  <svg class="abs cta-shape" viewBox="0 0 467 220" aria-hidden="true">
    <path d="M0 16 C0 10 4 7 9 9 C60 26 120 40 180 38 C280 33 380 6 455 7 C462 7 467 11 467 18 L467 208 C467 215 462 220 455 220 L12 220 C5 220 0 215 0 208 Z" fill="#5e93f3"/>
    <path d="M0 22 C0 16 4 13 9 15 C60 32 120 46 180 44 C280 39 380 12 455 13 C462 13 467 17 467 24 L467 208 C467 215 462 220 455 220 L12 220 C5 220 0 215 0 208 Z" fill="#1f3865"/>
  </svg>
  <div class="abs robot" role="img" aria-label="Glossy white robot kneeling while working on a laptop"></div>
  <h2 class="abs cta-title">Try <span class="accent">Quill Helper</span> Now – It's Free!</h2>
  <p class="abs cta-text" style="top:631px">Are you ready to elevate your business with the power of AI? Getting started is as easy as<br>entering your website URL into the box below. Within minutes, your Quill Helper will be<br>ready to take your customer support to the next level.</p>
  <p class="abs cta-text" style="top:670px">Don't wait to experience the future of customer interaction. Try Quill Helper now for free<br>and watch your business grow effortlessly. Click the button below to start your journey<br>with Quill Helper.</p>
  <div class="abs cta-button">Build my free website now!</div>

  <!-- FAQ -->
  <div class="abs center eyebrow" style="top:799px">FAQS</div>
  <h2 class="abs center section-title" style="top:808px">What They Often Ask About <span class="accent">Quill Helper</span>.</h2>
  <div class="abs rule" style="top:828px"></div>

  <div class="abs faq">
    <div class="faq-q" style="top:12px">How long does it take to set up Quill Helper?</div>
    <svg class="faq-toggle" style="top:13px" viewBox="0 0 6 6" stroke="#1d2431" stroke-width=".6"><path d="M0 3 H6 M3 0 V6"/></svg>
    <div class="faq-divider" style="top:29px"></div>
    <div class="faq-q open" style="top:38px">Is there a free plan available?</div>
    <svg class="faq-toggle" style="top:39px" viewBox="0 0 6 6" stroke="#1d2431" stroke-width=".6"><path d="M0 3 H6"/></svg>
    <p class="faq-a">Yes! We offer a free plan designed for smaller or newer businesses to get started with Quill Helper.</p>
    <div class="faq-divider" style="top:71px"></div>
    <div class="faq-q" style="top:81px">Can I add my own content to the bot's knowledgebase?</div>
    <svg class="faq-toggle" style="top:82px" viewBox="0 0 6 6" stroke="#1d2431" stroke-width=".6"><path d="M0 3 H6 M3 0 V6"/></svg>
    <div class="faq-divider" style="top:98px"></div>
    <div class="faq-q" style="top:107px">What if I want to interact directly with some customers without the bot's assistance?</div>
    <svg class="faq-toggle" style="top:108px" viewBox="0 0 6 6" stroke="#1d2431" stroke-width=".6"><path d="M0 3 H6 M3 0 V6"/></svg>
  </div>

  <p class="abs center closing">Start your journey with <span class="accent">Quill Helper</span> today and see why businesses of all sizes trust us to handle their<br>customer support needs. Your intelligent AI assistant is just a few clicks away – <span class="accent">try it now</span>!</p>

  <!-- Footer -->
  <footer class="abs footer">
    <div class="brand">Quill Helper</div>
    <p class="tagline">It'll take minutes or less! Just answer a few basic questions and watch your stunning new website generate in seconds!</p>
    <p class="copyright">© 2025 Quill Helper. All Rights Reserved</p>
    <div class="footer-col" style="left:248px">
      <h3>Navigation</h3>
      <ul>
        <li>About PageLoomX</li>
        <li>Affiliate Program</li>
        <li>Learn More About AI</li>
        <li>Make Money with PageLoomX</li>
        <li>The History of AI</li>
        <li>Pricing</li>
        <li>Blog</li>
        <li>Sitemap</li>
      </ul>
    </div>
    <div class="footer-col" style="left:359px">
      <h3>Contact Us</h3>
      <ul>
        <li>Terms &amp; Conditions</li>
        <li>FAQ</li>
        <li>Privacy Policy</li>
        <li>Contact Us</li>
      </ul>
    </div>
    <div class="footer-col" style="left:470px">
      <h3>Follow Us</h3>
      <div class="social" aria-label="Social links">
        <span></span><span></span><span></span><span></span><span></span>
        <span></span><span></span><span></span>
      </div>
    </div>
  </footer>

</div>
</body>
</html>
```